Brom-leigh Sky Harbour Custom Brokers Limited

Shop online from the USA and Ship to Jamaica
Customs Brokerage, Import Export and logistic Services
Address:- 238-240 Halden Brook Road Kingston Jamaica
Email: info@bromleighskyharbour,com
Web: www.bromleighskyharbour.com
Telephone: (876) 555-0148, (876) 555-0193
flyer should be quarter page must print information on back and front

```html
<!DOCTYPE html>
<html lang="en">
<head>
<meta charset="utf-8">
<title>Brom-leigh Sky Harbour Custom Brokers – Quarter Page Flyer</title>
<link href="https://fonts.googleapis.com/css2?family=Montserrat:ital,wght@0,400;0,600;0,700;0,800;1,700&family=Lato:wght@400;700&display=swap" rel="stylesheet">
<style>
  :root{
    --navy:#0d2a55;
    --navy-deep:#0a1f40;
    --navy-mid:#1a3a6b;
    --gold:#f0b114;
    --gold-light:#f7c948;
    --white:#ffffff;
    --grey:#8a8f99;
    --stage:#e9e9ec;
  }
  *{margin:0;padding:0;box-sizing:border-box}
  html,body{width:1200px;height:891px;overflow:hidden;background:var(--stage)}
  .canvas{position:relative;width:1200px;height:891px}
  .flyer{position:absolute;top:117px;width:451px;height:640px;overflow:hidden;box-shadow:0 6px 18px rgba(0,0,0,.25)}
  .flyer--front{left:129px;background:var(--white)}
  .flyer--back{left:619px;background:var(--white)}
  .flyer svg.art{position:absolute;inset:0;width:451px;height:640px}

  .brand{position:absolute;left:0;right:0;text-align:center;font-family:"Montserrat",sans-serif}
  .brand__mark{display:flex;align-items:center;justify-content:center;gap:10px;font-weight:800;font-size:46px;letter-spacing:2px}
  .brand__dot{width:22px;height:22px;border-radius:50%;background:var(--gold)}
  .brand__name{font-weight:700;font-size:16px;letter-spacing:.3px;margin-top:8px}
  .brand__sub{font-weight:400;font-size:10px;letter-spacing:6px;margin-top:1px}
  .flyer--front .brand{top:24px;color:var(--navy)}
  .flyer--front .brand__sub{color:var(--grey)}
  .flyer--back .brand{top:20px;color:var(--white)}
  .flyer--back .brand__mark{font-size:38px}
  .flyer--back .brand__name{font-size:14px;margin-top:6px}
  .flyer--back .brand__sub{font-size:8.5px;letter-spacing:5px}

  .headline{position:absolute;left:0;right:0;top:508px;text-align:center;font-family:"Montserrat",sans-serif;font-weight:800;color:var(--navy);line-height:1}
  .headline__top{font-size:35px;letter-spacing:-.3px}
  .headline__bottom{font-size:24.5px;margin-top:4px;letter-spacing:-.2px}
  .tagbar{position:absolute;left:24px;width:399px;top:577px;height:24px;border-radius:4px;background:linear-gradient(var(--gold-light),var(--gold));box-shadow:0 3px 3px rgba(0,0,0,.25);display:flex;align-items:center;justify-content:center;gap:4px;font-family:"Montserrat",sans-serif;font-style:italic;font-weight:700;font-size:14px;color:var(--navy-deep);white-space:nowrap}
  .tagbar__tick{width:11px;height:11px}
  .front-url{position:absolute;left:0;right:0;top:606px;text-align:center;font-family:"Montserrat",sans-serif;font-size:13px;letter-spacing:1.5px;color:var(--navy)}
  .front-url b{font-style:italic;font-weight:800}

  .services-pill{position:absolute;left:32px;top:121px;width:384px;height:27px;border-radius:14px;background:var(--white);text-align:center;font-family:"Montserrat",sans-serif;font-weight:800;font-size:18px;letter-spacing:4px;line-height:27px;color:var(--navy)}
  .services-pill span{color:var(--gold)}
  .service{position:absolute;left:0;width:451px;height:62px}
  .service__icon{position:absolute;left:54px;top:0;width:59px;height:59px;border-radius:50%;background:var(--gold);display:flex;align-items:center;justify-content:center}
  .service__icon svg{width:34px;height:34px;fill:none;stroke:var(--navy);stroke-width:2;stroke-linecap:round;stroke-linejoin:round}
  .service__title{position:absolute;left:133px;top:1px;font-family:"Montserrat",sans-serif;font-weight:700;font-size:15px;color:var(--gold);border-bottom:1.5px solid var(--gold);line-height:16px}
  .service__text{position:absolute;left:133px;top:19px;width:300px;font-family:"Lato",sans-serif;font-size:9px;line-height:11.6px;color:var(--white)}

  .contact{position:absolute;left:22px;font-family:"Montserrat",sans-serif;color:var(--navy);white-space:nowrap}
  .contact--phone{top:567px;font-weight:700;font-size:17.5px}
  .contact--web{top:589px;font-weight:700;font-size:17.5px;border-bottom:1.5px solid var(--navy);line-height:20px}
  .contact--address{top:613px;font-weight:600;font-size:10px}
</style>
</head>
<body>
<main class="canvas">

  <!-- FRONT -->
  <section class="flyer flyer--front">
    <svg class="art" viewBox="0 0 451 640">
      <defs>
        <linearGradient id="deliveryTone" x1="0" y1="0" x2="1" y2="0">
          <stop offset="0" stop-color="#1f6fc4"/>
          <stop offset=".45" stop-color="#c9a46a"/>
          <stop offset=".75" stop-color="#d8b27a"/>
          <stop offset="1" stop-color="#ece6dc"/>
        </linearGradient>
      </defs>
      <path role="img" aria-label="Photo of a courier handing parcels from online stores to a customer" fill="url(#deliveryTone)"
        d="M0,150 C90,205 200,200 300,172 C380,150 430,165 451,215 L451,470 C380,448 250,452 140,478 C80,492 30,470 0,425 Z"/>
      <path d="M0,110 C30,160 80,185 180,188 C100,196 40,185 0,150 Z" fill="var(--navy)"/>
      <path d="M120,190 C220,185 300,150 370,148 C420,147 445,180 451,215 L451,196 C440,160 410,138 360,140 C290,142 220,175 120,190 Z" fill="var(--gold)"/>
      <path d="M0,425 C30,470 80,492 140,478 C90,500 30,490 0,450 Z" fill="var(--gold)"/>
      <path d="M0,440 C40,500 110,505 180,488 C110,520 30,505 0,470 Z" fill="var(--gold)"/>
      <path d="M140,478 C250,452 380,448 451,470 L451,545 C430,505 370,475 300,475 C230,475 180,485 140,478 Z" fill="var(--navy)"/>
      <path d="M150,490 C250,470 330,466 390,478 C330,474 250,480 150,490 Z" fill="var(--gold)"/>
    </svg>
    <header class="brand">
      <div class="brand__mark"><span class="brand__dot"></span>BSH</div>
      <div class="brand__name">BROM-LEIGH SKY HARBOUR</div>
      <div class="brand__sub">Custom Brokers Ltd.</div>
    </header>
    <h1 class="headline">
      <div class="headline__top">SHOP ONLINE FROM</div>
      <div class="headline__bottom">THE USA &amp; SHIP TO JAMAICA</div>
    </h1>
    <div class="tagbar">Customs Brokerage
      <svg class="tagbar__tick" viewBox="0 0 12 12"><circle cx="6" cy="6" r="6" fill="#3a3a3a"/><path d="M3.2 6.2l1.9 1.9 3.7-3.9" stroke="#fff" stroke-width="1.5" fill="none"/></svg>
      Import Export
      <svg class="tagbar__tick" viewBox="0 0 12 12"><circle cx="6" cy="6" r="6" fill="#3a3a3a"/><path d="M3.2 6.2l1.9 1.9 3.7-3.9" stroke="#fff" stroke-width="1.5" fill="none"/></svg>
      logistic Services</div>
    <p class="front-url">www.<b>bromleighskyharbour</b>.com</p>
  </section>

  <!-- BACK -->
  <section class="flyer flyer--back">
    <svg class="art" viewBox="0 0 451 640">
      <defs>
        <linearGradient id="portTone" x1="0" y1="0" x2="1" y2="1">
          <stop offset="0" stop-color="#123063"/>
          <stop offset=".55" stop-color="#0f2950"/>
          <stop offset="1" stop-color="#1c3a5e"/>
        </linearGradient>
        <linearGradient id="officeTone" x1="0" y1="0" x2="1" y2="1">
          <stop offset="0" stop-color="#f3ece4"/>
          <stop offset=".5" stop-color="#b58a6a"/>
          <stop offset="1" stop-color="#7a5a44"/>
        </linearGradient>
      </defs>
      <rect role="img" aria-label="Background photo of a container port with a cargo ship" width="451" height="640" fill="url(#portTone)"/>
      <path d="M0,490 C30,540 90,560 170,552 C260,545 340,515 451,512 L451,640 L0,640 Z" fill="var(--white)"/>
      <path d="M0,480 C20,530 80,550 160,545 C240,540 310,515 390,505 C330,520 260,548 170,556 C90,562 25,540 0,505 Z" fill="var(--gold)"/>
      <path d="M160,545 C250,530 340,500 451,500 L451,512 C340,512 260,540 170,552 Z" fill="var(--navy)"/>
      <rect role="img" aria-label="Photo of a smiling woman shopping online at a laptop beside parcels" x="311" y="500" width="140" height="140" fill="url(#officeTone)"/>
    </svg>
    <header class="brand">
      <div class="brand__mark"><span class="brand__dot"></span>BSH</div>
      <div class="brand__name">BROM-LEIGH SKY HARBOUR</div>
      <div class="brand__sub">Custom Brokers Ltd.</div>
    </header>
    <h2 class="services-pill">OUR <span>SERVICES</span></h2>

    <article class="service" style="top:167px">
      <div class="service__icon"><svg viewBox="0 0 34 34"><rect x="4" y="9" width="17" height="14"/><path d="M21 13h6l4 5v5h-10z"/><circle cx="10" cy="25" r="2.5"/><circle cx="26" cy="25" r="2.5"/><path d="M2 12h5M2 16h4"/></svg></div>
      <h3 class="service__title">SHIPPING</h3>
      <p class="service__text">Varietates autem iniurasque fortunae facile veteres philosophorum praeceptis instituta vita superabat. Et quod est munus, quod opus sapientiaiuvat.</p>
    </article>
    <article class="service" style="top:239px">
      <div class="service__icon"><svg viewBox="0 0 34 34"><path d="M4 24V15l3-6h6v15"/><path d="M13 14h4v10"/><path d="M17 8v16h12"/><rect x="20" y="13" width="8" height="7"/><circle cx="7" cy="26" r="2.5"/><circle cx="14" cy="26" r="2.5"/></svg></div>
      <h3 class="service__title">LOGISTICS</h3>
      <p class="service__text">Varietates autem iniurasque fortunae facile veteres philosophorum praeceptis instituta vita superabat. Et quod est munus, quod opus sapientiaiuvat.</p>
    </article>
    <article class="service" style="top:309px">
      <div class="service__icon"><svg viewBox="0 0 34 34"><rect x="5" y="4" width="14" height="18"/><rect x="15" y="11" width="14" height="19"/><path d="M8 9h8M8 13h4M18 16h8M18 20h4M19 25l2 2 4-4"/></svg></div>
      <h3 class="service__title">CUSTOMS CLEARANCE</h3>
      <p class="service__text">Varietates autem iniurasque fortunae facile veteres philosophorum praeceptis instituta vita superabat. Et quod est munus, quod opus sapientiaiuvat.</p>
    </article>
    <article class="service" style="top:380px">
      <div class="service__icon"><svg viewBox="0 0 34 34"><circle cx="17" cy="17" r="6"/><path d="M11 17h12M17 11c-3 4-3 8 0 12M17 11c3 4 3 8 0 12"/><path d="M4 9l4-4M4 5h4v4M30 9l-4-4M30 5h-4v4M4 25l4 4M4 29h4v-4M30 25l-4 4M30 29h-4v-4"/></svg></div>
      <h3 class="service__title">EXPORT</h3>
      <p class="service__text">Varietates autem iniurasque fortunae facile veteres philosophorum praeceptis instituta vita superabat. Et quod est munus, quod opus sapientiaiuvat.</p>
    </article>
    <article class="service" style="top:450px">
      <div class="service__icon"><svg viewBox="0 0 34 34"><path d="M14 11H5v18h20v-8"/><path d="M10 23c2-8 8-11 15-11V7l6 7-6 7v-5c-6 0-11 2-15 7z"/></svg></div>
      <h3 class="service__title">IMPORTS</h3>
      <p class="service__text">Varietates autem iniurasque fortunae facile veteres philosophorum praeceptis instituta vita superabat. Et quod est munus, quod opus sapientiaiuvat.</p>
    </article>

    <p class="contact contact--phone">(876) 555-0148 | (876) 555-0193</p>
    <p class="contact contact--web">WWW.BROMLEIGHSKYHARBOUR.COM</p>
    <p class="contact contact--address">238-240 HALDEN BROOK ROAD KINGSTON JAMAICA</p>
  </section>

</main>
</body>
</html>
```